The Timber Loft

We need a business card design for our wardrobe company.
Please visit our website www.zorvelcabinets.com to get an idea of who we are.

```html
<!DOCTYPE html>
<html lang="en">
<head>
<meta charset="utf-8">
<title>The Timber Loft – Business Card</title>
<link rel="stylesheet" href="https://fonts.googleapis.com/css2?family=Lato:wght@400;700&family=Roboto:wght@700&display=swap">
<style>
  :root {
    --backdrop: #1c1c1c;
    --card: #ffffff;
    --gold: #8e7a55;
    --ink: #3a3a3a;
    --ink-dark: #1a1a1a;
  }
  * { margin: 0; padding: 0; box-sizing: border-box; }
  html, body {
    width: 1200px; height: 900px; overflow: hidden;
    background: var(--backdrop);
  }
  .canvas {
    position: relative; width: 1200px; height: 900px;
  }
  .business-card {
    position: absolute; left: 260px; top: 257px;
    width: 680px; height: 387px;
    background: var(--card);
    border-radius: 24px;
    box-shadow: 0 6px 24px rgba(0,0,0,0.5);
    font-family: "Lato", sans-serif;
    color: var(--ink);
  }
  .brand {
    position: absolute; right: 36px; top: 46px;
    display: flex; align-items: center; gap: 12px;
  }
  .brand-square {
    width: 46px; height: 46px; background: var(--gold);
  }
  .brand-text { text-align: center; }
  .brand-name {
    font-weight: 700; font-size: 14.5px; letter-spacing: 0.9px;
    color: var(--ink-dark); text-transform: uppercase;
  }
  .brand-tagline {
    font-weight: 700; font-size: 13px; color: var(--ink-dark);
    margin-top: 5px;
  }
  .person-name {
    position: absolute; left: 34px; top: 192px;
    font-family: "Roboto", sans-serif; font-weight: 700;
    font-size: 30px; line-height: 36px;
    color: var(--gold); letter-spacing: -0.3px;
  }
  .person-role {
    position: absolute; left: 34px; top: 229px;
    font-size: 23px; line-height: 28px; color: var(--ink);
  }
  .divider {
    position: absolute; left: 134px; top: 244px;
    width: 509px; height: 1.5px; background: var(--gold);
  }
  .contact-list {
    position: absolute; left: 33px; top: 283px;
    list-style: none; font-size: 17px; letter-spacing: 0.6px;
  }
  .contact-list li {
    display: flex; align-items: center; gap: 6px;
    height: 20.4px;
  }
  .contact-icon { width: 12px; height: 12px; flex: none; }
  .address {
    position: absolute; right: 36px; top: 323px;
    text-align: right; font-size: 17px; letter-spacing: 1.1px;
    line-height: 20.4px; font-style: normal;
  }
</style>
</head>
<body>
<main class="canvas">
  <section class="business-card">
    <header class="brand">
      <span class="brand-square" aria-hidden="true"></span>
      <div class="brand-text">
        <p class="brand-name">The Timber Loft</p>
        <p class="brand-tagline">Built to Hang Just Right</p>
      </div>
    </header>

    <h1 class="person-name">Dara Quillon</h1>
    <p class="person-role">Manager</p>
    <span class="divider" aria-hidden="true"></span>

    <ul class="contact-list">
      <li>
        <svg class="contact-icon" viewBox="0 0 12 12" aria-hidden="true"><path d="M2 1 L4 1 L5 3.5 L3.8 4.6 Q5 7 7.4 8.2 L8.5 7 L11 8 L11 10 Q10 11 8.5 11 Q2 9.5 1 3.5 Q1 2 2 1Z" fill="var(--gold)"/></svg>
        <span>555-210-3847</span>
      </li>
      <li>
        <svg class="contact-icon" viewBox="0 0 12 12" aria-hidden="true"><rect x="3" y="0.7" width="6.4" height="10.6" rx="1" fill="none" stroke="var(--gold)" stroke-width="1.2"/><rect x="5.4" y="9.3" width="1.6" height="0.9" fill="var(--gold)"/></svg>
        <span>555-318-6620</span>
      </li>
      <li>
        <svg class="contact-icon" viewBox="0 0 12 12" aria-hidden="true"><rect x="0.5" y="2.5" width="11" height="8" fill="var(--gold)"/><path d="M1.5 3.5 L6 7 L10.5 3.5" fill="none" stroke="#fff" stroke-width="1"/></svg>
        <span>info@zorvelcabinets.com</span>
      </li>
      <li>
        <svg class="contact-icon" viewBox="0 0 12 12" aria-hidden="true"><circle cx="6" cy="6" r="5.3" fill="var(--gold)"/><path d="M6 0.7 Q3 6 6 11.3 M6 0.7 Q9 6 6 11.3 M0.7 6 H11.3" fill="none" stroke="#fff" stroke-width="0.8"/></svg>
        <span>www.zorvelcabinets.com</span>
      </li>
    </ul>

    <address class="address">
      18-20 Halvery Brookmonte<br>
      Street 509213, USA
    </address>
  </section>
</main>
</body>
</html>
```